The Harbor Circle (By Line: Shaping Tomorrow with Steady Guidance)

I am seeking the design and creation of a”banner ad image” for my radio program entitled “The Harbor Circle.” The banner created should capture the look and feel of an image that reflects the vision statement below and that fosters the intent reflected by the principal goals listed below:

Vision statement

The Harbor Circle is a powerfully engaging platform for great conversations about leadership and leadership learning.

Goals

1. Build a community of listeners who will be made to feel invited and excited about being connected to the show, it host and its broader community of listeners.

2. Provide interesting, intelligent and meaningful conversations about leadership and learning by the host, invited guests, both in studio and online.
The banner should be one that speaks to/invites listeners to become members of a community of listeners seeking to listen to and learn about the subject of leadership and leadership improvement.

The acceptable (final) banner should be professional in image, style and substance. The Photo shop layered file is required so that the banner image can be altered and adapted for use in PDF or text documents.

Finally, it is a banner that I intend to repopulate across several medium’s, such as netvyne, pal page, etc. as a part of the process of establishing an image – brand – for the radio show as reflected the vision statement and goals.

While the target audience described is broad, it is anticipated that the primary listeners will be those who are leaders and serving in such roles as CEO’s, Vice Presidents, and other leaders in business, government and other local organizational capacities including students interested in learning about and discussing the subject of leadership.

Target Market(s)

Those who are interested in the topic of leadership and are actively engaged in leading as supervisors, managers and executives. These would be CEO, VP, and other C-level leaders in business, private and public sector organizations. It is also anticipated that those who are students of leadership learning will find my program a great resource.

Industry/Entity Type

Radio

Colors
3176b5
b768aa
d3a5cc

Requirements
Must have
• Be unique, attractive and capture the look and feel as noted in the description of the project.
Nice to have
• Note: I will have a head shot photo included in the banner so a place holder needs to be included for that

```html
<!DOCTYPE html>
<html lang="en">
<head>
<meta charset="utf-8">
<title>The Harbor Circle – Banner Ads</title>
<link rel="stylesheet" href="https://fonts.googleapis.com/css2?family=Open+Sans:wght@400;600;700;800&display=swap">
<style>
  :root {
    --canvas: #e4e4e4;
    --white: #ffffff;
    --navy: #0b1638;
    --navy-mid: #2a3f68;
    --sky: #dcebf2;
    --sky-mid: #9fb9cc;
    --slate: #5e7e98;
    --slate-light: #a6b8c5;
    --brand-blue: #3176b5;
    --brand-plum: #b768aa;
    --brand-rose: #d3a5cc;
    --link-blue: #0a6fc2;
  }
  * { box-sizing: border-box; margin: 0; padding: 0; }
  html, body {
    width: 1200px; height: 1200px; overflow: hidden;
    background: var(--canvas);
    font-family: "Open Sans", sans-serif;
  }
  .stage { position: relative; width: 1200px; height: 1200px; }

  .banner {
    position: absolute;
    background: var(--white);
    box-shadow: 0 9px 10px -6px rgba(0,0,0,0.5);
    overflow: hidden;
  }

  /* Photo area: team silhouettes before a grid window */
  .photo {
    position: relative;
    width: 100%;
    background:
      linear-gradient(180deg,
        var(--sky) 0%,
        var(--sky-mid) 28%,
        var(--navy-mid) 55%,
        var(--navy) 72%,
        #3d5878 82%,
        var(--navy) 100%);
  }
  .photo-fill { position: absolute; inset: 0; }

  .headshot {
    position: absolute;
    border-radius: 50%;
    background: radial-gradient(circle at 50% 40%, var(--brand-rose) 0%, var(--brand-plum) 100%);
    border: 2px solid var(--white);
    box-shadow: 0 0 0 2px var(--brand-blue);
  }

  .byline {
    position: absolute; left: 0; right: 0;
    color: var(--white);
    font-weight: 600;
    text-align: center;
    letter-spacing: 0.2px;
  }
  .byline::before {
    content: ""; display: block; margin: 0 auto;
    background: var(--brand-rose);
  }

  /* Medium rectangle */
  .banner--rect { left: 450px; top: 203px; width: 300px; height: 249px; }
  .banner--rect .photo { height: 213px; }
  .banner--rect .headshot { right: 12px; top: 12px; width: 54px; height: 54px; }
  .banner--rect .byline { bottom: 9px; font-size: 10px; }
  .banner--rect .byline::before { width: 40px; height: 2px; margin-bottom: 5px; }

  .rect-bar { position: relative; height: 36px; }
  .rect-bar .title-panel {
    position: absolute; left: 0; top: 0; bottom: 0; width: 180px;
    background: linear-gradient(90deg, var(--slate) 0%, var(--slate-light) 72%, var(--slate) 100%);
    clip-path: polygon(0 0, 100% 0, 94% 100%, 0 100%);
  }
  .rect-bar .divider { position: absolute; left: 168px; top: 0; width: 12px; height: 36px; }
  .rect-bar .title {
    position: absolute; left: 19px; top: 8px;
    color: var(--white); font-weight: 800; font-size: 14px; line-height: 20px;
  }
  .rect-bar .cta {
    position: absolute; left: 194px; top: 8px;
    color: var(--link-blue); font-size: 14px; line-height: 20px;
  }

  /* Half page */
  .banner--tall { left: 480px; top: 494px; width: 240px; height: 480px; }
  .banner--tall .photo { height: 360px; }
  .banner--tall .headshot { right: 14px; top: 14px; width: 72px; height: 72px; }
  .banner--tall .byline { bottom: 14px; padding: 0 18px; font-size: 12px; line-height: 16px; }
  .banner--tall .byline::before { width: 50px; height: 2px; margin-bottom: 7px; }

  .tall-title {
    height: 58px; display: flex; align-items: center; justify-content: center;
    background: linear-gradient(90deg, var(--slate) 0%, var(--slate-light) 50%, var(--slate) 100%);
    border-top: 3px solid var(--brand-blue);
    color: var(--white); font-weight: 800; font-size: 22px;
  }
  .tall-cta {
    height: 62px; display: flex; align-items: center; justify-content: center;
    color: var(--link-blue); font-size: 19px;
  }
</style>
</head>
<body>
<main class="stage">
  <section class="banner banner--rect">
    <div class="photo">
      <div class="photo-fill" role="img" aria-label="Blue-toned silhouettes of a team of leaders standing before a tall grid window, reflected on a glossy floor"></div>
      <div class="headshot" role="img" aria-label="Host headshot placeholder"></div>
      <p class="byline">By Line: Shaping Tomorrow with Steady Guidance</p>
    </div>
    <div class="rect-bar">
      <div class="title-panel"></div>
      <svg class="divider" viewBox="0 0 12 36" aria-hidden="true">
        <polygon points="8,0 12,0 5,36 1,36" fill="var(--brand-blue)"/>
      </svg>
      <span class="title">The Harbor Circle</span>
      <span class="cta">LEARN MORE</span>
    </div>
  </section>

  <section class="banner banner--tall">
    <div class="photo">
      <div class="photo-fill" role="img" aria-label="Blue-toned silhouettes of leaders with arms crossed before a grid window, reflected on a glossy floor"></div>
      <div class="headshot" role="img" aria-label="Host headshot placeholder"></div>
      <p class="byline">By Line: Shaping Tomorrow with Steady Guidance</p>
    </div>
    <div class="tall-title">The Harbor Circle</div>
    <div class="tall-cta">LEARN MORE</div>
  </section>
</main>
</body>
</html>
```